Film poster for The Lanterns Kept Burning - a documentary

We need a poster for our documentary, The Lanterns Kept Burning, about how Ancient heroine Veronel finds new life in Beirut’s refugee camps, helping four Syrian women discover the strength to live with joy through the greatest of tragedies. The film is about 20% animated with the rest being vérité footage shot in Beirut, Lebanon. The title will be in Arabic and English.

Please check out our trailer here: https://www.fundmeadow.example/projects/573816402/the-lanterns-kept-burning?ref=tkzp4m

We've included some assets from the film as well as style references of other film posters we've liked.

The designer we use will also get a credit in the film.

Target Market(s)

Documentary film festivals

Industry/Entity Type

Film Production

Font styles to use
Sans Serif

Colors

Designer to choose colors to be used in the design.

Requirements
Must have
• The Title in Both English and Arabic (Can provide the text for the arabic)
• Space at the bottom to overlay film credits
Nice to have
• Include the texture of the wall and perhaps integrate both photographic and graphic imagery
Should not have
• Shouldn't be too busy - minimalistic

```html
<!DOCTYPE html>
<html lang="en">
<head>
<meta charset="utf-8">
<title>The Lanterns Kept Burning — Poster</title>
<link rel="stylesheet" href="https://fonts.googleapis.com/css2?family=Oswald:wght@500;700&family=Passion+One:wght@700&family=Noto+Naskh+Arabic:wght@500&display=swap">
<style>
  :root {
    --backdrop: #e4e2de;
    --paper: #ffffff;
    --wash-sky: #cde8ea;
    --wash-cream: #f1ebdc;
    --wash-peach: #f4cfb3;
    --ink-teal: #2f5450;
    --ink-deep: #1f3d3e;
    --ink-soft: #5e7a63;
  }
  * { margin: 0; padding: 0; box-sizing: border-box; }
  html, body {
    width: 1200px; height: 1148px; overflow: hidden;
    background: var(--backdrop);
  }
  .poster {
    position: absolute; left: 170px; top: 24px;
    width: 860px; height: 1100px;
    background: var(--paper);
    box-shadow: 0 2px 10px rgba(0,0,0,0.08);
  }
  .wash {
    position: absolute; left: 58px; top: 58px;
    width: 744px; height: 984px;
    background: linear-gradient(180deg, var(--wash-sky) 0%, var(--wash-cream) 48%, var(--wash-peach) 100%);
    clip-path: polygon(0.6% 0.8%, 18% 0%, 40% 0.6%, 62% 0%, 85% 0.7%, 99.4% 0%, 100% 12%, 99.2% 30%, 100% 52%, 99.3% 74%, 100% 96%, 98% 100%, 72% 99.3%, 48% 100%, 25% 99.4%, 2% 100%, 0% 88%, 0.8% 64%, 0% 40%, 0.7% 20%);
  }
  .title-arabic {
    position: absolute; top: 132px; width: 100%;
    text-align: center; direction: rtl;
    font-family: "Noto Naskh Arabic", serif;
    font-weight: 500; font-size: 46px;
    color: var(--ink-deep);
  }
  .figure-art {
    position: absolute; left: 262px; top: 340px;
    width: 220px; height: 290px;
    border-radius: 48% 48% 12% 12% / 42% 42% 8% 8%;
    background: linear-gradient(160deg, #1f4a4e 0%, #2f5f5a 55%, #6a7e4e 100%);
  }
  .title-english {
    position: absolute; top: 710px; width: 100%;
    text-align: center; color: var(--ink-teal);
  }
  .title-kicker {
    display: block;
    font-family: "Oswald", sans-serif; font-weight: 700;
    font-size: 34px; letter-spacing: 1px; line-height: 1;
  }
  .title-main {
    display: block;
    font-family: "Passion One", sans-serif; font-weight: 700;
    font-size: 108px; line-height: 0.95; letter-spacing: 1px;
  }
  .credits {
    position: absolute; top: 858px; width: 100%;
    text-align: center; color: var(--ink-soft);
    font-family: "Oswald", sans-serif; font-weight: 500;
    font-size: 14px; line-height: 1.5;
  }
  .credits .credits-head { text-transform: uppercase; }
</style>
</head>
<body>
  <div class="poster">
    <div class="wash">
      <h2 class="title-arabic" lang="ar">ظلت الفوانيس مشتعلة</h2>
      <div class="figure-art" role="img" aria-label="Watercolour silhouette of a woman in a headscarf, its lower edge dissolving into a city skyline, in deep teal and olive tones"></div>
      <h1 class="title-english">
        <span class="title-kicker">THE LANTERNS KEPT</span>
        <span class="title-main">Burning</span>
      </h1>
      <div class="credits">
        <p class="credits-head">Film credits goes here</p>
        <p>The Title in Both English and Arabic (Can provide the text for the arabic)</p>
        <p>- Space at the bottom to overlay film credits. Nice to Have:</p>
      </div>
    </div>
  </div>
</body>
</html>
```